WE WOULD LIKE TO HAVE PROFESSIONAL LOOK ALLERGEN MATRIX DESIGN.
Our company is KANDRIX VENTURES LIMITED.
I am sharing a competitors design as well.
We would like to have grafics for 14 allergens. At the end of the allergen matrix we would like to have a like a list for review details and approval date. I am also attaching an example what we are using right now.
We would like to signs for may contain, contains, removable, additionally GMO and Colorant

```html
<!DOCTYPE html>
<html lang="en">
<head>
<meta charset="utf-8">
<title>Allergen Matrix – Kandrix Ventures Limited</title>
<link href="https://fonts.googleapis.com/css2?family=Arimo:wght@400;700&family=Montserrat:wght@300;700&family=Roboto+Condensed:wght@400&family=Tinos&display=swap" rel="stylesheet">
<style>
:root{
  --ink:#0b0b0c;
  --lime:#cad72a;
  --lime-dark:#8a9418;
  --lime-pale:#f0f4d6;
  --head-grey:#d4d5d8;
  --grid:#6a6a6a;
  --alert:#e0251b;
  --white:#ffffff;
}
*{box-sizing:border-box;margin:0;padding:0}
html,body{width:851px;height:1200px;overflow:hidden;background:var(--white)}
body{position:relative;font-family:Arimo,Arial,sans-serif;color:var(--ink)}
.top-bar{position:absolute;left:3px;top:39px;width:385px;height:29px;background:var(--ink)}
.top-accent{position:absolute;left:808px;top:39px;width:43px;height:29px;background:var(--lime)}
.brand{position:absolute;left:405px;top:30px;height:46px;display:flex;align-items:center;white-space:nowrap}
.brand-name{font-family:Montserrat,sans-serif;font-weight:700;font-size:31px;letter-spacing:5px;color:var(--ink)}
.brand-divider{width:1.5px;height:38px;background:var(--ink);margin:0 10px 0 6px}
.brand-tagline{font-family:Montserrat,sans-serif;font-weight:300;font-size:12.5px;letter-spacing:2.8px;line-height:19px;color:#333}
.page-title{position:absolute;left:54px;top:94px;font-size:32px;font-weight:400;letter-spacing:.3px}
.matrix{position:absolute;left:52px;top:135px;width:748px;border-collapse:collapse;table-layout:fixed;border:1.5px solid #444}
.matrix td,.matrix th{border:1px solid var(--grid);padding:0}
.dishes-head{background:var(--lime-pale);font-size:17px;font-weight:700;text-align:center}
.allergen-head{background:var(--head-grey);height:104px;vertical-align:bottom;padding-bottom:6px!important}
.allergen-head span{writing-mode:vertical-rl;transform:rotate(180deg);display:inline-block;font-size:14px;font-weight:700;line-height:13.5px;text-align:left}
.icon-cell{height:38px;text-align:center;vertical-align:middle}
.icon-cell svg{display:block;margin:auto}
.section td{background:var(--lime);height:24px;text-align:center;font-size:17px;font-weight:700}
.dish{font-family:"Roboto Condensed",sans-serif;font-size:14.5px;line-height:17.5px;padding-left:5px!important;text-align:left}
.alt .dish{background:var(--lime-pale)}
.matrix tbody td:not(.dish){text-align:center;font-size:14.5px}
.short td{height:21.5px}
.tall td{height:38.5px}
.salad td{height:23.8px}
.tick::before{content:"\2714"}
.may{font-family:Tinos,serif;font-size:12px!important;color:#333}
.may::before{content:"O"}
.revisions{position:absolute;left:52px;top:923px;width:748px;border-collapse:collapse;table-layout:fixed;border:1px solid #444}
.revisions th{background:var(--ink);color:var(--white);font-size:15px;font-weight:700;text-align:left;height:24px;padding-left:6px}
.revisions td{border:1px solid var(--grid);height:23.8px;font-size:15px;padding-left:6px}
.revisions td.num{text-align:center;padding-left:0}
.notes{position:absolute;left:52px;top:1040px;font-size:12px;line-height:15.3px}
.notes .warn{color:var(--alert)}
.notes .mark{color:var(--alert)}
.key{display:flex;align-items:center;gap:4px;white-space:nowrap}
.key-sign{display:inline-flex;align-items:center;justify-content:center;width:12px;height:12px}
.key-sign svg{display:block}
.contact-band{position:absolute;left:3px;top:1097px;width:848px;height:52px;background:var(--ink);display:flex;align-items:center;justify-content:center;gap:20px;color:var(--white);font-size:14px}
.contact{display:flex;align-items:center;gap:10px}
.contact-icon{width:24px;height:24px;border-radius:50%;background:var(--white);display:flex;align-items:center;justify-content:center}
.address-band{position:absolute;left:3px;top:1149px;width:848px;height:51px;background:var(--lime);text-align:center;line-height:51px;font-size:14px}
</style>
</head>
<body>
<div class="top-bar"></div>
<div class="brand">
  <span class="brand-name">KANDRIX</span>
  <span class="brand-divider"></span>
  <span class="brand-tagline">FOOD HYGIENE<br>HEALTH &amp; SAFETY</span>
</div>
<div class="top-accent"></div>

<h1 class="page-title">ALLERGEN MATRIX</h1>

<table class="matrix">
  <colgroup>
    <col style="width:168px"><col style="width:41px"><col style="width:46px"><col style="width:45px"><col style="width:42px"><col style="width:40px"><col style="width:41px"><col style="width:42px"><col style="width:41px"><col style="width:42px"><col style="width:40px"><col style="width:40px"><col style="width:43px"><col style="width:39px"><col style="width:38px">
  </colgroup>
  <thead>
    <tr>
      <th class="dishes-head" rowspan="2">DISHES</th>
      <th class="allergen-head"><span>Celery</span></th>
      <th class="allergen-head"><span>Cereals<br>containing<br>gluten</span></th>
      <th class="allergen-head"><span>Crustaceans</span></th>
      <th class="allergen-head"><span>Eggs</span></th>
      <th class="allergen-head"><span>Fish</span></th>
      <th class="allergen-head"><span>Lupin</span></th>
      <th class="allergen-head"><span>Milk</span></th>
      <th class="allergen-head"><span>Molluscs</span></th>
      <th class="allergen-head"><span>Mustard</span></th>
      <th class="allergen-head"><span>Nuts</span></th>
      <th class="allergen-head"><span>Peanuts</span></th>
      <th class="allergen-head"><span>Sesame<br>seeds</span></th>
      <th class="allergen-head"><span>Soya</span></th>
      <th class="allergen-head"><span>Sulphur<br>dioxide</span></th>
    </tr>
    <tr>
      <td class="icon-cell" aria-label="Celery"><svg width="26" height="26" viewBox="0 0 26 26"><circle cx="13" cy="13" r="11.5" fill="none" stroke="#c4d12a" stroke-width="1.6"/><path d="M11 7v12M15 7v12" stroke="#8a9418" stroke-width="1.3" fill="none"/></svg></td>
      <td class="icon-cell" aria-label="Gluten"><svg width="26" height="26" viewBox="0 0 26 26"><circle cx="13" cy="13" r="11.5" fill="none" stroke="#c4d12a" stroke-width="1.6"/><path d="M8 18l10-10" stroke="#8a9418" stroke-width="1.3"/><ellipse cx="14" cy="11" rx="2" ry="1" fill="#8a9418"/><ellipse cx="11" cy="14" rx="2" ry="1" fill="#8a9418"/></svg></td>
      <td class="icon-cell" aria-label="Crustaceans"><svg width="26" height="26" viewBox="0 0 26 26"><circle cx="13" cy="13" r="11.5" fill="none" stroke="#c4d12a" stroke-width="1.6"/><ellipse cx="13" cy="14" rx="5" ry="3.5" fill="none" stroke="#8a9418" stroke-width="1.3"/></svg></td>
      <td class="icon-cell" aria-label="Eggs"><svg width="26" height="26" viewBox="0 0 26 26"><circle cx="13" cy="13" r="11.5" fill="none" stroke="#c4d12a" stroke-width="1.6"/><ellipse cx="13" cy="13.5" rx="4.5" ry="5.5" fill="none" stroke="#8a9418" stroke-width="1.3"/></svg></td>
      <td class="icon-cell" aria-label="Fish"><svg width="26" height="26" viewBox="0 0 26 26"><circle cx="13" cy="13" r="11.5" fill="none" stroke="#c4d12a" stroke-width="1.6"/><path d="M7 13c3-4 8-4 10 0-2 4-7 4-10 0zM17 13l3-3v6z" fill="none" stroke="#8a9418" stroke-width="1.3"/></svg></td>
      <td class="icon-cell" aria-label="Lupin"><svg width="26" height="26" viewBox="0 0 26 26"><circle cx="13" cy="13" r="11.5" fill="none" stroke="#c4d12a" stroke-width="1.6"/><path d="M8 18l10-10" stroke="#8a9418" stroke-width="1.3"/><circle cx="12" cy="12" r="1.3" fill="#8a9418"/><circle cx="15" cy="10" r="1.3" fill="#8a9418"/></svg></td>
      <td class="icon-cell" aria-label="Milk"><svg width="26" height="26" viewBox="0 0 26 26"><circle cx="13" cy="13" r="11.5" fill="none" stroke="#c4d12a" stroke-width="1.6"/><rect x="10" y="8" width="6" height="11" rx="1.5" fill="none" stroke="#8a9418" stroke-width="1.3"/></svg></td>
      <td class="icon-cell" aria-label="Molluscs"><svg width="26" height="26" viewBox="0 0 26 26"><circle cx="13" cy="13" r="11.5" fill="none" stroke="#c4d12a" stroke-width="1.6"/><circle cx="13" cy="13" r="4.5" fill="none" stroke="#8a9418" stroke-width="1.3"/></svg></td>
      <td class="icon-cell" aria-label="Mustard"><svg width="26" height="26" viewBox="0 0 26 26"><circle cx="13" cy="13" r="11.5" fill="none" stroke="#c4d12a" stroke-width="1.6"/><path d="M12 7h2v3l2 3v6h-6v-6l2-3z" fill="none" stroke="#8a9418" stroke-width="1.3"/></svg></td>
      <td class="icon-cell" aria-label="Nuts"><svg width="26" height="26" viewBox="0 0 26 26"><circle cx="13" cy="13" r="11.5" fill="none" stroke="#c4d12a" stroke-width="1.6"/><circle cx="12" cy="12" r="3.5" fill="none" stroke="#8a9418" stroke-width="1.3"/><circle cx="16" cy="16" r="2" fill="none" stroke="#8a9418" stroke-width="1.3"/></svg></td>
      <td class="icon-cell" aria-label="Peanuts"><svg width="26" height="26" viewBox="0 0 26 26"><circle cx="13" cy="13" r="11.5" fill="none" stroke="#c4d12a" stroke-width="1.6"/><path d="M9 17c-2-2 0-4 2-5s1-4 4-4 3 3 1 5-3 0-4 3-2 2-3 1z" fill="none" stroke="#8a9418" stroke-width="1.3"/></svg></td>
      <td class="icon-cell" aria-label="Sesame"><svg width="26" height="26" viewBox="0 0 26 26"><circle cx="13" cy="13" r="11.5" fill="none" stroke="#c4d12a" stroke-width="1.6"/><g fill="none" stroke="#8a9418" stroke-width="1.1"><ellipse cx="10" cy="10" rx="1.5" ry="1"/><ellipse cx="16" cy="10" rx="1.5" ry="1"/><ellipse cx="13" cy="13" rx="1.5" ry="1"/><ellipse cx="10" cy="16" rx="1.5" ry="1"/><ellipse cx="16" cy="16" rx="1.5" ry="1"/></g></svg></td>
      <td class="icon-cell" aria-label="Soya"><svg width="26" height="26" viewBox="0 0 26 26"><circle cx="13" cy="13" r="11.5" fill="none" stroke="#c4d12a" stroke-width="1.6"/><path d="M8 18c2-6 6-9 10-10-1 5-4 9-10 10z" fill="none" stroke="#8a9418" stroke-width="1.3"/></svg></td>
      <td class="icon-cell" aria-label="Sulphur dioxide"><svg width="26" height="26" viewBox="0 0 26 26"><circle cx="13" cy="13" r="11.5" fill="none" stroke="#c4d12a" stroke-width="1.6"/><circle cx="13" cy="14" r="4.5" fill="none" stroke="#8a9418" stroke-width="1.3"/><path d="M13 9.5v-2" stroke="#8a9418" stroke-width="1.3"/></svg></td>
    </tr>
  </thead>
  <tbody>
    <tr class="section"><td colspan="15">Sandwiches &amp; Wraps</td></tr>
    <tr class="short"><td class="dish">Chicken Bacon Wrap</td><td class="tick"></td><td class="tick"></td><td></td><td class="tick"></td><td></td><td></td><td></td><td></td><td class="tick"></td><td></td><td></td><td></td><td></td><td></td></tr>
    <tr class="tall alt"><td class="dish">Cream Cheese, Salmon &amp;<br>Bagel</td><td></td><td class="tick"></td><td></td><td></td><td class="tick"></td><td></td><td class="tick"></td><td></td><td></td><td></td><td></td><td></td><td></td><td></td></tr>
    <tr class="tall"><td class="dish">Roasted Veggies, Mayo<br>Sauce, Ciabatta</td><td></td><td class="tick"></td><td></td><td class="tick"></td><td></td><td></td><td class="tick"></td><td></td><td class="tick"></td><td></td><td></td><td></td><td></td><td></td></tr>
    <tr class="tall alt"><td class="dish">Chicken Sandwich, Mayo<br>Sauce, Walnut, Potato Bun</td><td></td><td class="tick"></td><td></td><td class="tick"></td><td></td><td></td><td class="tick"></td><td></td><td class="tick"></td><td class="tick"></td><td></td><td></td><td></td><td class="may"></td></tr>
    <tr class="short"><td class="dish">Grilled Cheese Sandwich</td><td></td><td class="tick"></td><td></td><td></td><td></td><td></td><td class="tick"></td><td></td><td></td><td></td><td></td><td></td><td></td><td></td></tr>
    <tr class="tall alt"><td class="dish">Avocado on Toast with<br>Cheese Spread</td><td></td><td class="tick"></td><td></td><td></td><td></td><td></td><td class="tick"></td><td></td><td></td><td></td><td></td><td></td><td></td><td></td></tr>
    <tr class="short"><td class="dish">Spinach &amp; Tahini Pastry Roll</td><td></td><td class="tick"></td><td></td><td class="tick"></td><td></td><td></td><td class="tick"></td><td></td><td></td><td></td><td></td><td class="tick"></td><td></td><td></td></tr>
    <tr class="short alt"><td class="dish">Feta Cheese Pastry Roll</td><td></td><td class="tick"></td><td></td><td class="tick"></td><td></td><td></td><td class="tick"></td><td></td><td></td><td></td><td></td><td></td><td></td><td></td></tr>
    <tr class="short"><td class="dish">Feta Cheese &amp; Honey Pastry</td><td></td><td class="tick"></td><td></td><td class="tick"></td><td></td><td></td><td class="tick"></td><td></td><td></td><td></td><td></td><td class="tick"></td><td></td><td></td></tr>
    <tr class="short alt"><td class="dish">Chicken, Mayo, Mustard Wrap</td><td class="tick"></td><td class="tick"></td><td></td><td class="tick"></td><td></td><td></td><td></td><td></td><td class="tick"></td><td></td><td></td><td></td><td></td><td class="may"></td></tr>
    <tr class="short"><td class="dish">Falafel, Hummus Wrap</td><td></td><td class="tick"></td><td></td><td></td><td></td><td></td><td></td><td></td><td></td><td></td><td></td><td class="tick"></td><td></td><td></td></tr>
    <tr class="section"><td colspan="15">Salads &amp; Hot Lunch Meals</td></tr>
    <tr class="salad"><td class="dish">Bulgur Salad</td><td class="tick"></td><td class="tick"></td><td></td><td></td><td></td><td></td><td></td><td></td><td></td><td></td><td></td><td></td><td></td><td></td></tr>
    <tr class="salad alt"><td class="dish">Mung Bean Salad</td><td class="tick"></td><td></td><td></td><td></td><td></td><td></td><td></td><td></td><td></td><td></td><td></td><td></td><td></td><td></td></tr>
    <tr class="salad"><td class="dish">Black-eyed Beans Salad</td><td class="tick"></td><td></td><td></td><td></td><td></td><td></td><td></td><td></td><td></td><td></td><td></td><td></td><td></td><td class="tick"></td></tr>
    <tr class="salad alt"><td class="dish">Chickpeas Salad</td><td class="tick"></td><td></td><td></td><td></td><td></td><td></td><td></td><td></td><td></td><td></td><td></td><td></td><td></td><td></td></tr>
    <tr class="salad"><td class="dish">Peas Salad</td><td class="tick"></td><td></td><td></td><td></td><td></td><td></td><td></td><td></td><td></td><td></td><td></td><td></td><td></td><td></td></tr>
    <tr class="salad alt"><td class="dish">Carrot Salad</td><td class="tick"></td><td></td><td></td><td></td><td></td><td></td><td></td><td></td><td></td><td></td><td></td><td></td><td></td><td></td></tr>
    <tr class="salad"><td class="dish">Celeriac Salad</td><td class="tick"></td><td></td><td></td><td class="tick"></td><td></td><td></td><td class="tick"></td><td></td><td></td><td></td><td></td><td></td><td></td><td></td></tr>
    <tr class="salad alt"><td class="dish">Beetroot Salad</td><td class="tick"></td><td></td><td></td><td></td><td></td><td></td><td></td><td></td><td></td><td></td><td></td><td class="tick"></td><td></td><td></td></tr>
    <tr class="salad"><td class="dish">Shakshuka</td><td class="tick"></td><td class="tick"></td><td></td><td class="tick"></td><td></td><td></td><td></td><td></td><td></td><td></td><td></td><td></td><td></td><td></td></tr>
    <tr class="salad alt"><td class="dish">Ham&amp;Cheese Croissant</td><td class="may"></td><td class="tick"></td><td></td><td class="tick"></td><td></td><td class="may"></td><td class="tick"></td><td></td><td class="may"></td><td class="may"></td><td class="may"></td><td class="may"></td><td class="may"></td><td class="may"></td></tr>
    <tr class="salad"><td class="dish">Porridge with Oatmilk</td><td></td><td class="tick"></td><td></td><td></td><td></td><td></td><td></td><td></td><td></td><td></td><td class="may"></td><td></td><td></td><td></td></tr>
  </tbody>
</table>

<table class="revisions">
  <colgroup><col style="width:126px"><col style="width:129px"><col></colgroup>
  <thead><tr><th>Revision No</th><th>Revision Date</th><th>Explanation</th></tr></thead>
  <tbody>
    <tr><td class="num">00</td><td>13.10.2023</td><td>Preparation</td></tr>
    <tr><td class="num">02</td><td>14.10.2024</td><td>Butter beans salad has been added</td></tr>
    <tr><td class="num">03</td><td>18.10.2024</td><td>Removed this dish</td></tr>
  </tbody>
</table>

<div class="notes">
  <p class="warn">All above are shared for general guidance purposes. The Allergen list should be revised regularly.</p>
  <p class="warn">KANDRIX VENTURES LIMITED does not accept responsibility for potential allergen reactions.</p>
  <p class="key">
    <span>“<span class="mark">O</span>” (May Contain),</span>
    <span class="key-sign"><svg width="12" height="12" viewBox="0 0 12 12"><path d="M2 6.5l2.5 2.5L10 3" stroke="#0b0b0c" stroke-width="1.8" fill="none"/></svg></span><span>(Contains),</span>
    <span class="key-sign"><svg width="12" height="12" viewBox="0 0 12 12"><circle cx="6" cy="6" r="5" fill="none" stroke="#8a9418" stroke-width="1.3"/><path d="M3.3 6h5.4" stroke="#8a9418" stroke-width="1.4"/></svg></span><span>(Removable),</span>
    <span class="key-sign"><svg width="12" height="12" viewBox="0 0 12 12"><path d="M6 1l5 5-5 5-5-5z" fill="#cad72a" stroke="#8a9418" stroke-width="1"/></svg></span><span>(GMO)</span>
    <span class="key-sign"><svg width="12" height="12" viewBox="0 0 12 12"><path d="M6 1C4 4.5 2.8 6 2.8 7.8a3.2 3.2 0 0 0 6.4 0C9.2 6 8 4.5 6 1z" fill="#e0251b"/></svg></span><span>(Colorant)</span>
  </p>
</div>

<div class="contact-band">
  <div class="contact">
    <span class="contact-icon"><svg width="14" height="14" viewBox="0 0 14 14"><path d="M3 1.5l2 2.5-1 1.5c1 2 2.5 3.5 4.5 4.5l1.5-1 2.5 2-1.5 2C6 12.5 1.5 8 1 3z" fill="#c4d12a"/></svg></span>
    <span>+44 (0)20 3000 4127</span>
  </div>
  <div class="contact">
    <span class="contact-icon"><svg width="14" height="14" viewBox="0 0 14 14"><rect x="1" y="3" width="12" height="8" fill="#c4d12a"/><path d="M1 3l6 5 6-5" stroke="#fff" stroke-width="1" fill="none"/></svg></span>
    <span>info@kandrixventures.co.uk</span>
  </div>
  <div class="contact">
    <span class="contact-icon"><svg width="14" height="14" viewBox="0 0 14 14"><circle cx="7" cy="7" r="6" fill="#c4d12a"/><path d="M1 7h12M7 1c-3 3-3 9 0 12M7 1c3 3 3 9 0 12" stroke="#fff" stroke-width=".8" fill="none"/></svg></span>
    <span>www.kandrixventures.co.uk</span>
  </div>
</div>
<div class="address-band">42 Harrowden Lane. NW4 2QT. London UK</div>
</body>
</html>
```